E-Commerce Website Update for Bamboo Poles Company

Existing website at:

http://www.reedcraftstudio.example/
http://www.reedcraftstudio.example/pages/product-and-price-list

Two pages to design: home page and "price list" page.

Info for home page as follows:

HOME PAGE:

Header:
Company Name: reedcraft studio
Telephone: 1 888 412 5093

Across the top:
Home | Price List | Blog | FAQ | About | Contact

Down the side:
About Bamboo
Wedding Arbors
Bamboo For Flutes
Black Bamboo
Spotted Bamboo
Bamboo Carpentry
Photo Gallery
All Products & Prices
Blog
FAQ
About
Contact

Should have shopping cart and search buttons on top.
Please see ai file, attached for logo (leaf) and font
In addition the homepage should have one or two sections for promotions

Chosen design will be asked to help deign a PRODUCT AND PRICE LIST page similar to the one we have now, but with "LEARN MORE" and "ORDER NOW" buttons for each item.
Updates

Reason: Thanks  for all the designs so far; giving an extra week for extra consideration.

Target Market(s)

Consumers, wedding planners.

Industry/Entity Type

Shopping

Requirements
Must have
• Clean, easy to read design.
Should not have
• No flash animation.

```html
<!DOCTYPE html>
<html lang="en">
<head>
<meta charset="utf-8">
<title>reedcraft studio — Pole Provider</title>
<link rel="stylesheet" href="https://fonts.googleapis.com/css2?family=Gelasio&family=Noto+Sans:wght@400&family=Arimo&display=swap">
<style>
:root{
  --black:#111;
  --header-dark:#141414;
  --header-band:#2a2a2a;
  --green:#7cc242;
  --green-dark:#5f9a2c;
  --green-light:#a6d97a;
  --link-green:#6a9f2a;
  --sidebar-bg:#f1f1f1;
  --sidebar-border:#dcdcdc;
  --text:#111;
  --white:#fff;
}
*{box-sizing:border-box;margin:0;padding:0}
html,body{width:1200px;height:1200px;overflow:hidden;background:var(--white)}
.page{position:absolute;left:0;top:0;width:1020px;height:1020px;transform:scale(1.17647);transform-origin:0 0;font-family:"Noto Sans",Tahoma,sans-serif;color:var(--text)}

/* header */
.site-header{position:absolute;left:0;top:0;width:1020px;height:92px;background:linear-gradient(180deg,var(--header-dark) 0,var(--header-dark) 55px,var(--header-band) 75px,var(--header-dark) 92px)}
.header-rule{position:absolute;left:0;top:92px;width:1020px;height:6px;background:linear-gradient(180deg,var(--green) 0,var(--green-dark) 100%)}
.brand{position:absolute;left:40px;top:10px;display:flex;align-items:flex-start;gap:12px}
.brand-mark{width:62px;height:62px;border-radius:50%;background:var(--green);margin-top:2px;flex:none}
.brand-name{font-family:"Noto Sans",sans-serif;color:var(--white);font-size:24px;line-height:23px;width:130px}
.brand-phone{position:absolute;left:112px;top:61px;color:var(--white);font-size:16px;line-height:20px;letter-spacing:.2px}
.cart{position:absolute;left:638px;top:5px;display:flex;gap:8px;align-items:flex-start}
.cart-text{font-family:"Gelasio",serif;color:var(--green);font-size:12px;line-height:15px;width:118px}
.cart-divider{position:absolute;left:806px;top:4px;width:1px;height:32px;background:#333}
.search{position:absolute;left:820px;top:8px;width:158px;height:19px;background:var(--white);border-radius:10px;display:flex;align-items:center;gap:4px;padding-left:6px;font-family:Arimo,sans-serif;font-size:10px;color:#222}
.top-nav{position:absolute;left:480px;top:73px;display:flex;gap:6px}
.top-nav a{display:block;width:72px;height:19px;border-radius:6px 6px 0 0;background:linear-gradient(180deg,var(--green-light),var(--green));color:var(--white);text-decoration:none;font-size:13px;line-height:19px;text-align:center}
.top-nav a.is-current{background:linear-gradient(180deg,#cfeab8,var(--green-light))}

/* main */
.intro{position:absolute;left:40px;top:126px;width:642px}
.intro-title{font-size:23px;font-weight:400;margin-left:2px;letter-spacing:-.2px}
.hero{margin-top:10px;width:646px;height:232px;margin-left:-5px;border:5px solid #eee;background:radial-gradient(circle at 28% 18%,#f7ffd8 0,#c9e36a 14%,#86b428 38%,#4f7d16 70%,#2d4a0c 100%)}
.intro-copy{margin-top:12px;font-size:11px;line-height:15px;letter-spacing:-.15px}
.intro-copy p{margin-bottom:13px}
.intro-copy a{color:var(--link-green);text-decoration:none}
.intro-rule{position:absolute;left:42px;top:665px;width:638px;height:2px;background:var(--green)}

.side-menu{position:absolute;left:689px;top:128px;width:292px;height:545px;background:var(--sidebar-bg);border:1px solid var(--sidebar-border);padding:15px 8px 0 12px;font-family:"Gelasio",Georgia,serif}
.side-menu a{display:block;color:#333;text-decoration:none;font-size:17.5px;line-height:23px;border-bottom:1px solid #fff;box-shadow:0 1px 0 #e4e4e4;margin-bottom:7px}

/* promos */
.promo{position:absolute;top:691px;width:460px}
.promo-one{left:39px}
.promo-two{left:521px}
.promo-head{height:37px;background:linear-gradient(180deg,#6a6a6a 0,#2a2a2a 60%,#3a3a3a 100%);border-bottom:3px solid var(--green);font-family:Arimo,Arial,sans-serif;font-weight:400;color:var(--green);font-size:22px;line-height:33px}
.promo-one .promo-head{padding-left:25px}
.promo-two .promo-head{padding-left:14px}
.promo-tab{width:0;height:0;border-top:7px solid var(--green-dark);border-right:7px solid transparent}
.promo-body{font-family:Arimo,Arial,sans-serif;font-size:13.4px;line-height:16.8px;padding:0 14px 0 9px;margin-top:-6px}
.promo-two .promo-body{padding-left:10px}
.promo-rule{position:absolute;top:196px;left:4px;width:454px;height:2px;background:var(--green)}
.promo-two .promo-rule{left:11px;width:454px}
.promo-split{position:absolute;left:510px;top:682px;width:1px;height:252px;background:#eee}

/* footer */
.site-footer{position:absolute;left:0;top:942px;width:1020px;height:78px;background:linear-gradient(180deg,var(--black) 0,var(--black) 50px,#262626 66px,var(--black) 78px)}
.footer-brand{position:absolute;left:40px;top:8px;display:flex;gap:8px;align-items:center}
.footer-brand .brand-mark{width:34px;height:34px;margin:0}
.footer-brand .brand-name{font-size:20px;line-height:19px;width:110px}
.footer-nav{position:absolute;top:6px;left:0;width:1020px;font-size:14px;color:var(--white)}
.footer-nav a{position:absolute;color:var(--white);text-decoration:none}
</style>
</head>
<body>
<div class="page">

<header class="site-header">
  <div class="brand">
    <span class="brand-mark"></span>
    <span class="brand-name">reedcraft studio</span>
  </div>
  <div class="brand-phone">1 888 412 5093</div>

  <div class="cart">
    <svg width="32" height="24" viewBox="0 0 32 24" aria-hidden="true">
      <path d="M1 3h5l4 13h16l4-10H8" fill="none" stroke="#7cc242" stroke-width="3" stroke-linejoin="round"/>
      <rect x="9" y="7" width="19" height="8" fill="#7cc242"/>
      <circle cx="12" cy="21" r="2.5" fill="#7cc242"/>
      <circle cx="24" cy="21" r="2.5" fill="#7cc242"/>
    </svg>
    <span class="cart-text">Your Cart is currently empty.</span>
  </div>
  <div class="cart-divider"></div>

  <div class="search">
    <svg width="16" height="11" viewBox="0 0 16 11" aria-hidden="true">
      <circle cx="5" cy="5" r="3.5" fill="none" stroke="#222" stroke-width="1.6"/>
      <path d="M7.5 7.5l2.5 2.5M11 4l2 2 2-2" fill="none" stroke="#222" stroke-width="1.4"/>
    </svg>
    Search
  </div>

  <nav class="top-nav">
    <a class="is-current" href="#">home</a>
    <a href="#">price list</a>
    <a href="#">blog</a>
    <a href="#">FAQ</a>
    <a href="#">about</a>
    <a href="#">contact</a>
  </nav>
</header>
<div class="header-rule"></div>

<main>
  <section class="intro">
    <h1 class="intro-title">Welcome to your Pole Provider 1 888 412 5093</h1>
    <div class="hero" role="img" aria-label="Sunlit bamboo forest with tall green stalks"></div>
    <div class="intro-copy">
      <p>Bamboo poles at wholesale prices direct from <a href="#">reedcraft studio.</a></p>
      <p>Need bamboo poles at a competitive price? Welcome to your one-stop pole shop.<br>
      We warehouse a variety of types poles in a variety of diameters, from 5/8" to 5 1/2", in lengths up to 8′.<br>
      We have natural poles, moso (mao) timber poles, black poles spotted poles… and regular bamboo poles. Whatever your project may be, from flutes to weddings to roasting a pig, we have the perfect pole for you.</p>
      <p>Poles are warehoused in Los Angeles, and ready for immediate shipping by ParcelRun ground to all of the United States. Or, if you’re in the SoCal area, you can collect your poles at our warehouse (see our FAQs).</p>
      <p>For our complete list of products with prices, please click here.</p>
      <p>Take advantage of our online shop for easy ordering. If you have any questions, contact us by calling us anytime at 1.888.412.5093 or email us at hello@reedcraftstudio.example.</p>
      <p>If you prefer to purchase our poles through Tradepost, or want to see feedback information about our product, please visit our Tradepost site here.</p>
    </div>
  </section>
  <div class="intro-rule"></div>

  <nav class="side-menu">
    <a href="#">About Bamboo</a>
    <a href="#">Wedding Arbors</a>
    <a href="#">Bamboo For Flutes</a>
    <a href="#">Black Bamboo</a>
    <a href="#">Spotted Bamboo</a>
    <a href="#">Bamboo Carpentry</a>
    <a href="#">Photo Gallery</a>
    <a href="#">All Products &amp; Prices</a>
    <a href="#">Blog</a>
    <a href="#">About</a>
    <a href="#">Contact</a>
  </nav>

  <div class="promo-split"></div>
  <section class="promo promo-one">
    <h2 class="promo-head">Promo Area 1</h2>
    <div class="promo-tab"></div>
    <p class="promo-body">Lorem ipsum dolor sit amet, consectetur adipiscing elit. Maecenas vel libero mi, eget pulvinar ligula. Suspendisse id semper lacus. Donec iaculis fermentum feugiat. Morbi imperdiet, eros et auctor varius, purus enim porta libero, a consequat sem mi eu risus. Nam fermentum, erat ac ullamcorper pretium, elit turpis ullamcorper massa, nec hendrerit eros ligula at felis. Praesent in risus sollicitudin justo convallis luctus et venenatis mauris. Etiam pretium placerat magna. Pellentesque rhoncus consectetur mollis.</p>
    <div class="promo-rule"></div>
  </section>
  <section class="promo promo-two">
    <h2 class="promo-head">Promo Area 2</h2>
    <div class="promo-tab"></div>
    <p class="promo-body">Lorem ipsum dolor sit amet, consectetur adipiscing elit. Maecenas vel libero mi, eget pulvinar ligula. Suspendisse id semper lacus. Donec iaculis fermentum feugiat. Morbi imperdiet, eros et auctor varius, purus enim porta libero, a consequat sem mi eu risus. Nam fermentum, erat ac ullamcorper pretium, elit turpis ullamcorper massa, nec hendrerit eros ligula at felis. Praesent in risus sollicitudin justo convallis luctus et venenatis mauris. Etiam pretium placerat magna. Pellentesque rhoncus consectetur mollis.</p>
    <div class="promo-rule"></div>
  </section>
</main>

<footer class="site-footer">
  <div class="footer-brand">
    <span class="brand-mark"></span>
    <span class="brand-name">reedcraft studio</span>
  </div>
  <nav class="footer-nav">
    <a href="#" style="left:551px">home</a>
    <a href="#" style="left:621px">price list</a>
    <a href="#" style="left:711px">blog</a>
    <a href="#" style="left:789px">FAQ</a>
    <a href="#" style="left:862px">about</a>
    <a href="#" style="left:935px">contact</a>
  </nav>
</footer>

</div>
</body>
</html>
```